Velvet Horizons 2 EP - Album Cover ARTwork

I need an album cover ARTWORK for my new digital EP. Emphasis on the word ART ! It has to be artistic,creative & inspiring.NOT marketing stuff.It has to be minimal & clean.I make TRIBAL music which combines primitive\primal\ancient rhythms with new techy electronica.Listen here : https://tunecloudia.example/moonwarpaudio
moonwarpaudio.example

Cover must include :
1.Title : Velvet Horizons 2 EP
2.My logo ( attached )

Use your imagination,inspiration & design mastery to visualize VELVET HORIZONS !

Target Market(s)

Digital Music

Industry/Entity Type

Digital

Requirements
Must have
• 1.Title : Velvet Horizons 2 EP
• 2.My logo ( attached )

```html
<!DOCTYPE html>
<html lang="en">
<head>
<meta charset="utf-8">
<title>Velvet Horizons 2 EP – Cover</title>
<link rel="stylesheet" href="https://fonts.googleapis.com/css2?family=Stint+Ultra+Condensed&family=Lato:wght@400&display=swap">
<style>
  :root {
    --stage: #0d0f12;
    --paper: #e9e7e2;
    --paper-shade: #d6d3cc;
    --ink: #1b1b1b;
    --logo: #c7321f;
    --fire-deep: #8e1410;
    --fire-red: #d52a1c;
    --fire-orange: #ee6a1a;
    --fire-gold: #f5b52a;
    --cool-blue: #2b3f8f;
  }
  * { margin: 0; padding: 0; box-sizing: border-box; }
  html, body {
    width: 1200px; height: 821px; overflow: hidden;
    background: var(--stage);
  }
  .canvas {
    position: relative; width: 1200px; height: 821px;
  }
  .cover {
    position: absolute; left: 220px; top: 30px;
    width: 760px; height: 760px;
    background:
      radial-gradient(ellipse at 30% 25%, rgba(255,255,255,0.55), transparent 60%),
      radial-gradient(ellipse at 75% 85%, rgba(0,0,0,0.06), transparent 55%),
      radial-gradient(circle at 50% 50%, var(--paper) 40%, var(--paper-shade) 100%);
    overflow: hidden;
  }
  .brand {
    position: absolute; left: 0; right: 0; top: 62px;
    text-align: center;
    font-family: "Lato", sans-serif; font-weight: 400;
    font-size: 40px; letter-spacing: 6px;
    color: var(--logo);
  }
  .title {
    position: absolute; left: 150px; top: 160px;
    font-family: "Stint Ultra Condensed", serif;
    font-weight: 400;
    line-height: 0.82;
    background: linear-gradient(135deg,
      var(--fire-deep) 0%, var(--fire-red) 22%, var(--fire-orange) 40%,
      var(--fire-red) 52%, var(--fire-gold) 62%, var(--fire-red) 74%,
      var(--cool-blue) 88%, var(--fire-deep) 100%);
    -webkit-background-clip: text; background-clip: text;
    color: transparent;
  }
  .title-line { display: block; }
  .title-line--first { font-size: 250px; letter-spacing: 2px; }
  .title-line--second { font-size: 225px; letter-spacing: -1px; }
  .edition {
    position: absolute; left: 455px; top: 580px;
    font-family: "Lato", sans-serif; font-weight: 400;
    font-size: 38px; letter-spacing: 2px;
    color: var(--ink);
  }
</style>
</head>
<body>
  <main class="canvas">
    <section class="cover" aria-label="Velvet Horizons 2 EP album cover">
      <div class="brand">MOONWARP</div>
      <h1 class="title">
        <span class="title-line title-line--first">Velvet</span>
        <span class="title-line title-line--second">Horizons</span>
      </h1>
      <div class="edition">2 EP</div>
    </section>
  </main>
</body>
</html>
```